KTR Engineering Business Card Design

We’re looking for an elegant, clean, and timeless business card design that communicates experience, capability, and reliability.

KTR Engineering was established in 1995 , we are a Government Contracting company providing Professional Services to the Ministry of Harbor Works, Frontier Stewardship and the Waypoint Consortium. Our capabilities include: Acquisition & Program Management; Intelligence & Security Operations; Cyber, IT & Network Operations; Lifecycle Logistics & Asset Readiness; C5ISR Systems Engineering & Sustainment.

We want the card to reflect a straightforward, confident approach to business. The design should feel polished and professional without being flashy or overly corporate.

Design Direction
Clean, sophisticated, and uncluttered
Elegant but understated
Strong typography and thoughtful spacing
A timeless aesthetic rather than something overly trendy
Confident and established, with a sense of substance
Easy to read and practical in a real-world business setting

The overall impression should be: “These are experienced professionals who know what they’re doing, do what they say, and can be relied upon.”

We’re open to creative interpretations. The finished card should feel distinctive through its typography, proportions, layout, and attention to detail rather than through excessive graphics or visual effects.

We’re looking for a design that would make a potential client immediately feel that they’re dealing with a capable, trustworthy, and established company.

Company Colors: Navy and Gold/Yellow (but you do not need to use these colors on the card)
Company Name: KTR Engineering Associates, Inc. (known as KTR Engineering)
Website: ktrengineering.example
Company Logo: Navy & Gold (other variations attached)

```html
<!DOCTYPE html>
<html lang="en">
<head>
<meta charset="utf-8">
<title>KTR Engineering Business Card</title>
<link rel="stylesheet" href="https://fonts.googleapis.com/css2?family=Red+Hat+Display:wght@400;500;700;900&display=swap">
<style>
  :root {
    --navy: #222b5e;
    --gold: #f6d94a;
    --card-light: #f0f0f2;
    --page: #ffffff;
    --white: #ffffff;
    --muted-white: #dfe2ef;
  }
  * { margin: 0; padding: 0; box-sizing: border-box; }
  html, body {
    width: 1200px; height: 1200px; overflow: hidden;
    background: var(--page);
    font-family: "Red Hat Display", Arial, sans-serif;
  }
  .canvas { position: relative; width: 1200px; height: 1200px; }

  .card {
    position: absolute;
    width: 438px; height: 259px;
    box-shadow: 6px 6px 10px rgba(0,0,0,0.14);
  }

  /* Front card */
  .card-front { left: 140px; top: 139px; background: var(--card-light); color: var(--navy); }
  .front-mark {
    position: absolute; right: 40px; top: 40px;
    display: flex; align-items: center; gap: 6px;
  }
  .mark-dot { width: 9px; height: 9px; border-radius: 50%; background: var(--gold); }
  .front-mark .mark-name { font-weight: 900; font-size: 28px; color: var(--navy); letter-spacing: 0.5px; }

  .person-name {
    position: absolute; left: 42px; top: 106px;
    font-weight: 700; font-size: 32px; letter-spacing: 0.5px; line-height: 1;
  }
  .person-title {
    position: absolute; left: 40px; top: 145px;
    font-weight: 400; font-size: 12px; letter-spacing: 0.1px;
  }
  .contact-list { position: absolute; left: 42px; top: 175px; list-style: none; }
  .contact-item {
    display: flex; align-items: center; gap: 10px;
    font-size: 16px; line-height: 20px; font-weight: 400;
  }
  .contact-icon { width: 14px; height: 14px; flex: none; }

  /* Back card */
  .card-back { left: 622px; top: 138px; background: var(--navy); color: var(--white); text-align: center; }
  .back-mark {
    position: absolute; left: 0; right: 0; top: 80px;
    display: flex; justify-content: center; align-items: center; gap: 10px;
  }
  .back-mark .mark-dot { width: 14px; height: 14px; }
  .back-mark .mark-name { font-weight: 900; font-size: 54px; line-height: 1; color: var(--white); letter-spacing: 1px; }
  .company-name {
    position: absolute; left: 0; right: 0; top: 165px;
    font-size: 11px; letter-spacing: 1.6px; font-weight: 500; color: var(--muted-white);
  }
  .company-site {
    position: absolute; left: 0; right: 0; top: 182px;
    font-size: 10.5px; letter-spacing: 1.2px; font-weight: 500; color: var(--muted-white);
  }
</style>
</head>
<body>
<main class="canvas">
  <section class="card card-front" aria-label="Business card front">
    <div class="front-mark">
      <span class="mark-name">KTR</span>
      <span class="mark-dot"></span>
    </div>
    <h1 class="person-name">MARLEN OKAFOR</h1>
    <p class="person-title">SENIOR SOFTWARE ENGINEER</p>
    <ul class="contact-list">
      <li class="contact-item">
        <svg class="contact-icon" viewBox="0 0 14 14" aria-hidden="true">
          <circle cx="7" cy="7" r="6" fill="var(--navy)"/>
          <path d="M5 4.2c.3-.2.6-.1.8.2l.5.8c.1.3 0 .5-.2.7l-.3.2c.3.8.9 1.4 1.6 1.8l.3-.3c.2-.2.5-.2.7-.1l.8.5c.3.2.3.5.1.8-.4.6-1 .8-1.6.5C6.5 8.6 5.4 7.5 4.8 6c-.2-.7 0-1.4.2-1.8z" fill="var(--card-light)"/>
        </svg>
        <span>555 01 274</span>
      </li>
      <li class="contact-item">
        <svg class="contact-icon" viewBox="0 0 14 14" aria-hidden="true">
          <rect x="0.5" y="3" width="13" height="8.5" fill="var(--navy)"/>
          <path d="M1 3.5 L7 8 L13 3.5" stroke="var(--card-light)" stroke-width="1" fill="none"/>
        </svg>
        <span>info@ktrengineering.example</span>
      </li>
    </ul>
  </section>

  <section class="card card-back" aria-label="Business card back">
    <div class="back-mark">
      <span class="mark-name">KTR</span>
      <span class="mark-dot"></span>
    </div>
    <p class="company-name">KTR ENGINEERING ASSOCIATES, INC.</p>
    <p class="company-site">ktrengineering.example</p>
  </section>
</main>
</body>
</html>
```